Business card design for Velvet Harbor

We need business cards designed for our new marketing consulting company, Velvet Harbor. Our services include marketing strategy, go-to-market and launch planning, growth strategy, and execution. We serve medical technology and health technology companies, from startups to well-established growth companies.

The business cards should feel professional, credible, reliable and trustworthy, and should instill confidence. Also bold, creative, and modern.

The design must use the Velvet Harbor logo.

The primary brand color is this orange: #FF5501
A secondary color that you can use is this gray: #282B2D
I would prefer only to use the orange and gray. But if you feel you really need an additional accent color (please use it very sparingly, as little as possible), you can use this blue for small accent purposes: #009FED

Attached are the logo files. The main logo is the one with a little bit of orange on the left and the rest is gray.

The business card should include the following:

Velvet Harbor logo
First name and last name
Title
Email address
Phone number and type (in whatever order looks best for the design
Website (the website does not need to be in the same block as the personal info)

For example:

Nessa Pryle
Founder & Principal
nessa@velvetharbor.com
+1.628.309.4156 mobile (can use "." or spaces in between blocks of numbers)
velvetharbor.com (somewhere on the card, it does not need to be with the personal info; and note that there is no "www." at the beginning)

Note that there will be no address listed on the business card.

Target Market(s)

Executives (CEO, head of marketing, head of sales) at medical technology and health technology companies, mostly in their 40s and older, well-educated, often with advanced degrees. They are strategic thinkers, responsible for budgets, and familiar with P&L. Their comfort with and trust in using outside consultants varies.

Industry/Entity Type

Medical technology and health technology companies.

Contact Information for Business Card

See project description

Font styles to use
Sans Serif

Requirements
Must have
• Logo and see Business card details section above.

```html
<!DOCTYPE html>
<html lang="en">
<head>
<meta charset="utf-8">
<title>Velvet Harbor — Business Card</title>
<link href="https://fonts.googleapis.com/css2?family=Jost:wght@400;500;600&display=swap" rel="stylesheet">
<style>
  :root {
    --backdrop: #808080;
    --card: #ffffff;
    --ink: #282b2d;
    --orange: #ff5501;
  }
  * { box-sizing: border-box; margin: 0; padding: 0; }
  html, body {
    width: 1200px; height: 1000px; overflow: hidden;
    background: var(--backdrop);
    font-family: "Jost", sans-serif;
    color: var(--ink);
  }
  .card {
    position: absolute;
    left: 294px; width: 613px; height: 352px;
    background: var(--card);
    border-radius: 28px;
    box-shadow: 0 24px 50px rgba(0,0,0,0.28);
    overflow: hidden;
  }
  .card--front { top: 121px; }
  .card--back { top: 532px; }

  .wordmark {
    position: absolute;
    display: flex; align-items: center; gap: 14px;
  }
  .wordmark__dot {
    border-radius: 50%;
    background: var(--orange);
    flex: none;
  }
  .wordmark__name {
    font-weight: 500;
    text-transform: uppercase;
    color: var(--ink);
    line-height: 1;
  }

  .card--front .wordmark { left: 0; right: 0; top: 140px; justify-content: center; }
  .card--front .wordmark__dot { width: 18px; height: 18px; }
  .card--front .wordmark__name { font-size: 38px; letter-spacing: 6px; }

  .website {
    position: absolute; left: 0; right: 0; top: 307px;
    text-align: center; font-size: 17px; letter-spacing: 0.3px;
  }
  .website__domain { color: var(--orange); font-weight: 500; }
  .website__tld { color: var(--ink); }

  .card--back .wordmark { left: 41px; top: 62px; gap: 10px; }
  .card--back .wordmark__dot { width: 12px; height: 12px; }
  .card--back .wordmark__name { font-size: 25px; letter-spacing: 4px; }

  .person { position: absolute; left: 41px; top: 194px; }
  .person__name { font-size: 21px; font-weight: 600; letter-spacing: 0.5px; line-height: 26px; }
  .person__title {
    font-size: 13px; color: var(--orange); text-transform: uppercase;
    letter-spacing: 0.6px; line-height: 16px;
  }
  .contact { position: absolute; left: 41px; top: 262px; list-style: none; }
  .contact__item {
    display: flex; align-items: center; gap: 7px;
    font-size: 19px; line-height: 25px;
  }
  .contact__icon { width: 16px; height: 18px; flex: none; }
</style>
</head>
<body>
  <section class="card card--front">
    <div class="wordmark">
      <span class="wordmark__dot"></span>
      <span class="wordmark__name">Velvet Harbor</span>
    </div>
    <p class="website"><span class="website__domain">velvetharbor</span><span class="website__tld">.com</span></p>
  </section>

  <section class="card card--back">
    <div class="wordmark">
      <span class="wordmark__dot"></span>
      <span class="wordmark__name">Velvet Harbor</span>
    </div>
    <div class="person">
      <h1 class="person__name">Nessa Pryle</h1>
      <p class="person__title">Founder &amp; Principal</p>
    </div>
    <ul class="contact">
      <li class="contact__item">
        <svg class="contact__icon" viewBox="0 0 16 18" aria-hidden="true">
          <rect x="0.5" y="4" width="15" height="10.5" fill="#ff5501"/>
          <path d="M1 4.6 L8 10 L15 4.6" fill="none" stroke="#fff" stroke-width="1.3"/>
          <path d="M1 14 L6 9 M15 14 L10 9" fill="none" stroke="#fff" stroke-width="1.1"/>
        </svg>
        nessa@velvetharbor.com
      </li>
      <li class="contact__item">
        <svg class="contact__icon" viewBox="0 0 16 18" aria-hidden="true">
          <rect x="2.5" y="0.8" width="10" height="16.4" rx="1.6" fill="none" stroke="#ff5501" stroke-width="1.6"/>
          <circle cx="7.5" cy="14.2" r="1" fill="#ff5501"/>
        </svg>
        +1.628.309.4156
      </li>
    </ul>
  </section>
</body>
</html>
```